Coffee and Plastics

I am looking for a completely new site that shows the products we have. Our current site is www.morvelbrewsupply.com. We are open minded to what designers come up with. Our current site is www.morvelbrewsupply.com. You can you the information from there to start the site. I need these tabs on the main home page. ( Home, Coffee & Tea, Condiments, and Paper and Plastics, and Contact.) You can take photos and info from my Current site. In products page.
I will be uploading info and photo for paper and plastics.
Look and feel
Each slider illustrates characteristics of the customer's brand and the style your logo design should communicate.

```html
<!DOCTYPE html>
<html lang="en">
<head>
<meta charset="utf-8">
<title>Morvel Brew Supply</title>
<link href="https://fonts.googleapis.com/css2?family=Open+Sans:wght@400;600;700;800&family=Oswald:wght@400;500;700&display=swap" rel="stylesheet">
<style>
:root{
  --brown:#6e3d22;
  --brown-dark:#3b2418;
  --brown-deep:#2a1910;
  --orange:#e9761c;
  --blue:#2a88c6;
  --ink:#333;
  --muted:#8a8a8a;
  --line:#e2e2e2;
  --bg:#ffffff;
  --hero-a:#f1efec;
  --hero-b:#c9c6c2;
  --photo-a:#e8e3dd;
  --photo-b:#b9aa9a;
}
*{box-sizing:border-box;margin:0;padding:0}
html,body{width:744px;height:1200px;overflow:hidden;background:var(--bg)}
body{font-family:"Open Sans",Arial,sans-serif;color:var(--ink);font-size:10px;position:relative}
.wrap{width:600px;margin:0 auto;position:relative}
.topbar{height:20px;background:#1e1e1e;color:#ddd;font-size:8px}
.topbar .wrap{display:flex;justify-content:space-between;align-items:center;height:20px}
.topbar nav span{margin-left:12px}
.header{height:68px}
.header .wrap{display:flex;justify-content:space-between;height:68px;align-items:center}
.logo-name{font-family:"Oswald",sans-serif;font-weight:700;font-size:22px;color:var(--brown);letter-spacing:.5px}
.logo-tag{font-size:8px;color:var(--muted);border-top:1px solid var(--line);margin-top:2px;padding-top:2px}
.header-tools{text-align:right;font-size:8px;color:#555}
.header-tools .row{display:flex;gap:8px;justify-content:flex-end;align-items:center;margin-bottom:6px}
.search{width:120px;height:16px;border:1px solid #ccc;display:flex;justify-content:space-between;align-items:center;padding:0 4px;color:#999}
.mainnav{height:24px;background:var(--brown)}
.mainnav .wrap{display:flex;justify-content:space-between;align-items:center;height:24px}
.mainnav ul{display:flex;list-style:none}
.mainnav li{color:#fff;font-size:9px;font-weight:600;padding:0 14px;line-height:24px;border-right:1px solid rgba(255,255,255,.2)}
.mainnav li.active{background:var(--brown-dark)}
.callus{color:#fff;font-family:"Oswald",sans-serif;font-size:11px;display:flex;align-items:center;gap:5px}
.hero{height:210px;background:linear-gradient(90deg,var(--hero-a),var(--hero-b));position:relative}
.hero .wrap{height:210px;display:flex}
.hero-text{width:250px;padding-top:30px}
.hero-text h1{font-family:"Oswald",sans-serif;font-weight:400;font-size:16px;color:var(--ink)}
.hero-text h2{font-family:"Oswald",sans-serif;font-weight:500;font-size:24px;color:var(--brown);margin-bottom:10px}
.hero-text li{list-style:none;font-size:8px;color:#555;margin-bottom:5px;display:flex;gap:6px;align-items:center}
.hero-text li::before{content:"";width:6px;height:6px;background:var(--orange)}
.btn{display:inline-block;background:var(--brown);color:#fff;font-size:9px;padding:6px 12px;border-radius:3px;margin-top:10px}
.hero-photo{position:absolute;top:0;right:0;width:430px;height:210px;background:linear-gradient(135deg,var(--photo-a),var(--photo-b))}
.features{height:50px;background:#f5f5f5;border-bottom:1px solid var(--line)}
.features .wrap{display:flex;height:50px}
.feature{flex:1;display:flex;align-items:center;gap:8px;padding-left:14px;border-right:1px solid var(--line)}
.feature b{display:block;font-size:11px;color:var(--brown)}
.feature small{font-size:7px;color:var(--muted)}
.promos{display:flex;gap:10px;margin-top:14px;height:124px}
.promo{flex:1;position:relative;padding:14px}
.promo-offer{background:#fff;border:1px solid var(--line)}
.promo-offer h3{font-family:"Oswald",sans-serif;font-weight:400;font-size:18px;color:var(--brown);line-height:1.1}
.promo-offer p{font-size:11px;margin-top:10px}
.promo-offer strong{font-family:"Oswald",sans-serif;font-size:20px;color:var(--orange)}
.promo-hours{background:linear-gradient(135deg,#5a4a40,#2b211c);color:#fff;text-align:center;font-family:"Oswald",sans-serif;padding-top:24px}
.promo-hours p{font-size:20px;line-height:1.15}
.promo-ground{background:var(--orange);color:#fff;font-family:"Oswald",sans-serif;text-align:right}
.promo-ground h3{font-size:20px;font-weight:500;line-height:1.1}
.promo-ground p{font-size:16px;margin-top:8px}
.promo-ground strong{font-size:26px}
.section-title{text-align:center;font-family:"Oswald",sans-serif;font-weight:400;font-size:15px;color:var(--ink);margin:16px 0 10px}
.products{display:flex;gap:14px}
.product{flex:1}
.product-img{height:72px;border:1px solid var(--line);background:linear-gradient(#fafafa,#e4e4e4)}
.product-meta{display:flex;justify-content:space-between;align-items:center;margin-top:6px;font-size:8px}
.price{color:var(--blue);font-size:12px;font-weight:700}
.shop{display:inline-block;border:1px solid #bbb;font-size:7px;padding:2px 6px;margin-top:4px}
.lower{position:absolute;top:845px;left:72px;width:600px;display:flex;gap:20px;height:130px}
.video{width:170px}
.video h4{font-size:9px;margin-bottom:6px;color:#555;font-weight:600}
.video-frame{height:96px;background:linear-gradient(90deg,#c8b8a8,#8a7564);position:relative}
.history{flex:1}
.history h3{font-family:"Oswald",sans-serif;font-weight:400;font-size:16px;margin-bottom:6px}
.history p{font-size:8px;color:#666;line-height:1.6}
.footer{position:absolute;top:987px;left:0;width:744px;height:178px;background:var(--brown-dark);color:#cbb9ac}
.footer .wrap{display:flex;gap:18px;padding-top:18px}
.fcol{flex:1;font-size:7.5px;line-height:1.7}
.fcol h5{font-family:"Oswald",sans-serif;font-weight:400;font-size:11px;color:#fff;margin-bottom:6px;border-bottom:1px solid rgba(255,255,255,.15);padding-bottom:4px}
.field{background:#fff;height:14px;margin-bottom:5px;color:#999;padding-left:4px;line-height:14px}
.field.tall{height:30px}
.send{display:inline-block;background:var(--orange);color:#fff;padding:2px 8px}
.cards{display:flex;gap:4px;margin-bottom:10px}
.cards span{width:26px;height:16px;background:#ddd;border-radius:2px}
.bottombar{position:absolute;top:1165px;left:0;width:744px;height:35px;background:var(--brown-deep);color:#a99;font-size:7.5px}
.bottombar .wrap{display:flex;justify-content:space-between;align-items:center;height:35px}
.bottombar nav span{margin-left:12px}
</style>
</head>
<body>
<div class="topbar"><div class="wrap"><span>Welcome to Morvel Brew Supply</span><nav><span>My Account</span><span>My Wishlist</span><span>My Cart</span><span>Checkout</span><span>Log In</span></nav></div></div>

<header class="header"><div class="wrap">
  <div><div class="logo-name">MORVEL BREW SUPPLY</div><div class="logo-tag">Serving fine brews since 1982</div></div>
  <div class="header-tools">
    <div class="row"><svg width="12" height="10" viewBox="0 0 12 10"><path d="M0 1h2l2 6h6l1-4H3" fill="none" stroke="#6e3d22" stroke-width="1.2"/><circle cx="5" cy="9" r="1" fill="#6e3d22"/><circle cx="9" cy="9" r="1" fill="#6e3d22"/></svg><span>0 item(s) - $0.00</span></div>
    <div class="row"><span>English</span><span>US Dollar</span></div>
    <div class="row"><div class="search"><span>Search</span><svg width="8" height="8" viewBox="0 0 8 8"><circle cx="3.2" cy="3.2" r="2.4" fill="none" stroke="#777"/><path d="M5 5l2.5 2.5" stroke="#777"/></svg></div></div>
  </div>
</div></header>

<div class="mainnav"><div class="wrap">
  <ul><li class="active">HOME</li><li>COFFEE</li><li>EQUIPMENT</li><li>GIFT</li><li>DISTRIBUTORS</li><li>ABOUT US</li></ul>
  <div class="callus"><svg width="10" height="10" viewBox="0 0 10 10"><path d="M2 1l2 2-1 1.5c.7 1.3 1.5 2 2.5 2.5L7 6l2 2-1.5 1.5C4 9 1 6 .5 2.5z" fill="#fff"/></svg>CALL US NOW : 1-800-555-0142</div>
</div></div>

<section class="hero">
  <div class="hero-photo" role="img" aria-label="Photo of a cappuccino cup with latte art on a saucer"></div>
  <div class="wrap">
  <div class="hero-text">
    <h1>Welcome To</h1>
    <h2>Morvel Brew Supply</h2>
    <ul>
      <li>Fresh roasted beans delivered to your door</li>
      <li>Premium brewing equipment for every kitchen</li>
      <li>Expert selection of teas and condiments</li>
      <li>Bulk pricing for offices and cafes</li>
    </ul>
    <span class="btn">View All Product</span>
  </div>
</div></section>

<section class="features"><div class="wrap">
  <div class="feature"><svg width="22" height="16" viewBox="0 0 22 16"><rect x="0" y="2" width="13" height="9" fill="#e9761c"/><path d="M13 5h5l3 3v3h-8z" fill="#e9761c"/><circle cx="5" cy="13" r="2" fill="#6e3d22"/><circle cx="17" cy="13" r="2" fill="#6e3d22"/></svg><div><b>Fast Service</b><small>Free Delivery</small></div></div>
  <div class="feature"><svg width="18" height="18" viewBox="0 0 18 18"><path d="M1 9l8-8h8v8l-8 8z" fill="#e9761c"/><circle cx="13" cy="5" r="1.5" fill="#fff"/></svg><div><b>Lowest Price</b><small>Guaranteed</small></div></div>
  <div class="feature"><svg width="16" height="18" viewBox="0 0 16 18"><rect x="1" y="8" width="14" height="10" fill="#e9761c"/><path d="M4 8V5a4 4 0 018 0v3" fill="none" stroke="#6e3d22" stroke-width="2"/></svg><div><b>Secure</b><small>Safe Checkout</small></div></div>
  <div class="feature"><svg width="18" height="18" viewBox="0 0 18 18"><circle cx="9" cy="9" r="8" fill="#e9761c"/><path d="M5 9l3 3 5-6" fill="none" stroke="#fff" stroke-width="2"/></svg><div><b>Satisfaction</b><small>Guaranteed</small></div></div>
</div></section>

<main class="wrap">
  <div class="promos">
    <div class="promo promo-offer"><h3>Our Special<br>Coffee Offer</h3><p>Starting <strong>$5.45</strong>/month</p></div>
    <div class="promo promo-hours" role="img" aria-label="Dark coffee shop background behind opening hours"><p>Mon To FRI<br>09:00 To 05:00<br>Central Time</p></div>
    <div class="promo promo-ground"><h3>Freshly Ground<br>Coffee</h3><p>Just <strong>$1.00</strong></p></div>
  </div>

  <h2 class="section-title">Featured Products</h2>
  <div class="products">
    <div class="product"><div class="product-img" role="img" aria-label="Paper coffee cups"></div><div class="product-meta"><span>Coffee no 1</span><span class="price">$ 7.45</span></div><span class="shop">Shop now</span></div>
    <div class="product"><div class="product-img" role="img" aria-label="White plastic compartment tray"></div><div class="product-meta"><span>Coffee no 2</span><span class="price">$ 7.45</span></div><span class="shop">Shop now</span></div>
    <div class="product"><div class="product-img" role="img" aria-label="Brown compartment food tray"></div><div class="product-meta"><span>Coffee no 3</span><span class="price">$ 7.45</span></div><span class="shop">Shop now</span></div>
    <div class="product"><div class="product-img" role="img" aria-label="Plastic food containers"></div><div class="product-meta"><span>Coffee no 4</span><span class="price">$ 7.45</span></div><span class="shop">Shop now</span></div>
    <div class="product"><div class="product-img" role="img" aria-label="White plastic cutlery"></div><div class="product-meta"><span>Coffee no 5</span><span class="price">$ 7.45</span></div><span class="shop">Shop now</span></div>
  </div>
</main>

<section class="lower">
  <div class="video"><h4>Our Latest Video</h4><div class="video-frame" role="img" aria-label="Video still of coffee being served"><svg width="170" height="96" viewBox="0 0 170 96"><circle cx="85" cy="48" r="14" fill="rgba(255,255,255,.8)"/><path d="M80 40l12 8-12 8z" fill="#6e3d22"/></svg></div></div>
  <div class="history"><h3>Our History</h3>
    <p>Our family began roasting coffee in a small shop with one drum roaster and a handful of loyal neighbours. Over the years we grew into a trusted supplier of beans, teas, condiments, paper goods and plastics for homes, offices and cafes across the region. Every order is packed with the same care we gave our very first customers, and we still taste every roast before it leaves our warehouse. Quality and service remain at the heart of all we do.</p>
  </div>
</section>

<footer class="footer"><div class="wrap">
  <div class="fcol"><h5>WELCOME</h5><p>We supply fresh coffee, fine teas and every paper and plastic item your break room needs. Orders ship quickly from our central warehouse with friendly support on every call.</p></div>
  <div class="fcol"><h5>SITE LINKS</h5><p>Home (we start here)<br>About (get to know us)<br>Services (all we do)<br>Coffee &amp; Tea shop<br>Blog (the news)<br>Contact (get in touch)</p></div>
  <div class="fcol"><h5>QUICK CONTACT</h5><div class="field">Name</div><div class="field">Email</div><div class="field tall">Message</div><span class="send">Send</span></div>
  <div class="fcol"><h5>PAYMENT OPTIONS</h5><div class="cards"><span></span><span></span><span></span><span></span></div><h5>OUR OFFICE</h5><p>Morvel Brew Supply<br>120 Roaster Lane, Suite 4<br>Springfield, TX 75000<br>Phone: 1-800-555-0142</p></div>
</div></footer>
<div class="bottombar"><div class="wrap"><span>COPYRIGHT © MORVEL BREW SUPPLY. ALL RIGHTS RESERVED</span><nav><span>HOME</span><span>ABOUT</span><span>GALLERY</span><span>CONTACT</span></nav></div></div>
</body>
</html>
```